KelvaNest - Home Income and Business Resources Platform

I am looking for a website template for a multi-purposed website. This website will feature:

1.) Website Directory with Ratings & comments on listings
2.) Company Blog
3.) Homepage with Content (see files for homepage mock)

I would like the Design to have a default width 1170px (wider then normal)

Of course I am looking for Pages for Listings to be designed.

Great looking BLOG Layout: http://journal.pixelvorn.example/html/blog.html

I would like 4 Versions of a Website Directory Listing "Box"
1.) Basic Listing Box
2.) Sponsored Listing Box
3.) Recommended Listing Box
4.) Stay Away From Listing Box

Information on the Listing Page (Like on a Category Page)
Site Name, Site URL, Website Image, # of Views, Rating and # of Comments

Information on the Listing Details Page:
Same as ABOVE + About website Description, Trovix Rank, Category Information

Decent looking examples is here: https://demos.quendaro.example/directory/computers/ and http://www.zibrankhub.example/.

I will include some sketches and screenshots of things I like/looking for. As designers,you have creative freedom and are encouraged to show this. This is Phase one of this project and winning designer is guaranteed to have future work for this project.

Target Market(s)

Directory, business, websites

Industry/Entity Type

Business

Font styles to use
Sans Serif

Colors

Designer to choose colors to be used in the design.

Requirements
Must have
• Professional yet clean look. The use of Icons & images
• Unique Look
Should not have
• Any exact copies of any examples I provided

```html
<!DOCTYPE html>
<html lang="en">
<head>
<meta charset="utf-8">
<title>KelvaNest</title>
<link rel="stylesheet" href="https://fonts.googleapis.com/css2?family=Lato:wght@400;700&display=swap">
<style>
:root{
  --sky-top:#2cc0f2;
  --sky-bottom:#0b6a9c;
  --white:#ffffff;
  --link:#1a73c8;
  --body-text:#666b70;
  --panel-head-a:#2a86d6;
  --panel-head-b:#1a6ac0;
  --rule:rgba(255,255,255,0.18);
}
*{box-sizing:border-box;margin:0;padding:0}
html,body{width:1200px;height:902px;overflow:hidden}
body{
  position:relative;font-family:"Lato",sans-serif;
  background:radial-gradient(ellipse at 80% 10%,#6fd8f6 0%,transparent 40%),
             linear-gradient(180deg,var(--sky-top) 0%,#1694cc 55%,var(--sky-bottom) 100%);
  color:var(--white);
}
.brand{position:absolute;left:99px;top:24px;font-size:31px;font-weight:700}
.menu{position:absolute;right:100px;top:31px;font-size:16px;font-weight:700;display:flex;align-items:center;gap:10px;color:#e8f7ff}
.hero{position:absolute;left:99px;top:83px;width:769px;height:297px;overflow:hidden}
.hero .photo{position:absolute;inset:0;background:linear-gradient(110deg,#c9b8a4 0%,#8f8a86 35%,#3d4f66 60%,#1e2a3a 100%)}
.hero h1{position:absolute;left:290px;top:172px;font-size:39px;line-height:46px;font-weight:700;text-shadow:0 2px 6px rgba(0,0,0,.6);white-space:nowrap}
.hero p{position:absolute;left:290px;top:226px;width:475px;font-size:19.5px;line-height:30px;font-weight:700;letter-spacing:-0.3px;text-shadow:0 2px 6px rgba(0,0,0,.6)}
.card{position:absolute;top:399px;width:247px;height:385px;background:var(--white)}
.card .photo{height:193px}
.card h2{margin:22px 10px 0 18px;font-size:15.5px;line-height:24px;font-weight:400;color:var(--link);white-space:nowrap;letter-spacing:-0.2px}
.card p{margin:10px 14px 0 19px;font-size:12.6px;line-height:24px;color:var(--body-text)}
.card a{display:block;margin:8px 19px 0;font-size:12.6px;color:var(--link)}
.sponsors{position:absolute;left:886px;top:83px;width:215px;height:472px;background:var(--white)}
.panel-head{background:linear-gradient(180deg,var(--panel-head-a),var(--panel-head-b));color:var(--white)}
.sponsors .panel-head{height:53px;padding:12px 23px;font-size:22px}
.sponsor{position:absolute;left:22px;width:167px;height:93px;background:var(--white);box-shadow:0 1px 4px rgba(0,0,0,.18);display:flex;align-items:center;justify-content:center;gap:8px;font-size:17px;font-weight:700;color:#2b3440}
.sponsor .dot{width:12px;height:12px;border-radius:50%}
.ad{position:absolute;left:886px;top:570px;width:215px;height:214px;background:var(--white);overflow:hidden}
.ad .panel-head{height:34px;padding:9px 8px;font-size:12.5px;font-weight:700;display:flex;justify-content:space-between}
.ad .photo{height:180px;background:linear-gradient(135deg,#e9e4d8 0%,#d83a3a 45%,#3fa44a 75%,#c02430 100%)}
.ad .close{position:absolute;right:0;bottom:0;width:110px;height:32px;background:#1c8ae0;color:var(--white);font-size:12.5px;display:flex;align-items:center;justify-content:space-between;padding:0 8px}
.footer-rule{position:absolute;left:99px;top:829px;width:1002px;border-top:1px solid var(--rule)}
.copyright{position:absolute;left:0;top:859px;width:1200px;text-align:center;font-size:14px}
</style>
</head>
<body>
<div class="brand">KelvaNest</div>
<div class="menu">Menu
  <svg width="19" height="16" viewBox="0 0 19 16"><rect y="0" width="19" height="3" fill="#fff"/><rect y="6.5" width="19" height="3" fill="#fff"/><rect y="13" width="19" height="3" fill="#fff"/></svg>
</div>

<section class="hero">
  <div class="photo" role="img" aria-label="Business team meeting around a table"></div>
  <h1>About KelvaNest</h1>
  <p>Lorem ipsum dolor sit amet, consectetur adipiscing elit. Morbi egestas arcu vel quam consequat.</p>
</section>

<article class="card" style="left:99px">
  <div class="photo" role="img" aria-label="Colleagues reviewing documents together" style="background:linear-gradient(135deg,#d9a57e,#8a5a40,#c6836a)"></div>
  <h2>Home Income<br>&amp; Business Resources directory</h2>
  <p>Find what you need, when you need it.The KelvaNest website directory is your one-stop.</p>
  <a href="#">Read More...</a>
</article>
<article class="card" style="left:359px">
  <div class="photo" role="img" aria-label="Hand signing a contract with a pen" style="background:linear-gradient(135deg,#f0f0ee,#c9c9c6,#2b3a50)"></div>
  <h2>Advertising<br>Benefits</h2>
  <p>Everyone needs to advertise and we know just how to get your offer out to the right people</p>
  <a href="#">Read More...</a>
</article>
<article class="card" style="left:620px">
  <div class="photo" role="img" aria-label="Hands holding a fan of banknotes" style="background:linear-gradient(135deg,#f2f2f2,#d8b49a,#8a6a7a)"></div>
  <h2>Earning With<br>KelvaNest</h2>
  <p>Join KelvaNest and start earning money. When you share KelvaNest and lock..</p>
  <a href="#">Read More...</a>
</article>

<aside class="sponsors">
  <div class="panel-head">Sponsors List</div>
  <div class="sponsor" style="top:62px"><span class="dot" style="background:#d3304a"></span>Farline Co</div>
  <div class="sponsor" style="top:164px"><span class="dot" style="background:#5aa832"></span>Tidewell</div>
  <div class="sponsor" style="top:266px"><span class="dot" style="background:#b0308a"></span>Quorva</div>
  <div class="sponsor" style="top:368px"><span class="dot" style="background:#6a2ea0"></span>Brimsoft</div>
</aside>

<aside class="ad">
  <div class="panel-head"><span>Add By Someone</span>
    <svg width="12" height="12" viewBox="0 0 12 12"><circle cx="6" cy="6" r="6" fill="#fff"/><rect x="5.2" y="5" width="1.6" height="4.5" fill="#1a6ac0"/><circle cx="6" cy="3.2" r="0.9" fill="#1a6ac0"/></svg>
  </div>
  <div class="photo" role="img" aria-label="Food offers promotional banner"></div>
  <div class="close">Close This Ad <span>✖</span></div>
</aside>

<div class="footer-rule"></div>
<div class="copyright">Copyright ©  2017 - KelvaNest.Allrights Reserved.</div>
</body>
</html>
```